Ridgeline Build Network Inc. Letterhead

Creation of attractive and eye catching letterhead for a business start-up for the construction industry. Letterhead must relate to construction, but avoid standard hammer and tools in the design.
Updates

I forgot to add some details, sorry about that. Some pertinent info: Ph: 916-555-0148 ridgelinebuildnet.example 487 Willowmere Ave, Ste 210 Folsom, CA 95699 info@ridgelinebuildnet.example not sure if slogan should be in there" “Connecting construction professionals to create a purpose driven industry.” must be able to be used in word. Thanks!

```html
<!DOCTYPE html>
<html lang="en">
<head>
<meta charset="utf-8">
<title>Ridgeline Build Network Inc. Letterhead</title>
<link href="https://fonts.googleapis.com/css2?family=Source+Sans+3:wght@400;600;700&display=swap" rel="stylesheet">
<style>
  :root {
    --navy: #1f2152;
    --red: #be2026;
    --paper: #ffffff;
    --backdrop: #e4e4e6;
    --ink: #26262c;
    --ghost-grey: #e9eaee;
  }
  * { margin: 0; padding: 0; box-sizing: border-box; }
  html, body { width: 1200px; height: 1000px; overflow: hidden; }
  body {
    background: var(--backdrop);
    font-family: "Source Sans 3", "Helvetica Neue", Arial, sans-serif;
    color: var(--ink);
    position: relative;
    -webkit-font-smoothing: antialiased;
  }
  .letterhead {
    position: absolute;
    width: 470px;
    height: 664px;
    background: var(--paper);
    overflow: hidden;
  }
  .letterhead--filled { left: 109px; top: 174px; }
  .letterhead--blank { left: 608px; top: 176px; }

  .corner { position: absolute; display: block; }
  .corner--top { left: 0; top: 0; width: 160px; height: 143px; }
  .corner--bottom { right: 0; bottom: 0; width: 113px; height: 98px; }

  .backdrop-mark {
    position: absolute;
    left: 40px; top: 150px;
    width: 400px; height: 430px;
  }

  .brand {
    position: absolute;
    right: 42px; top: 28px;
    width: 150px;
    text-align: center;
  }
  .brand__badge {
    width: 22px; height: 22px;
    margin: 0 auto 30px;
    background: var(--red);
  }
  .brand__name {
    font-weight: 700;
    font-size: 11.5px;
    line-height: 13px;
    letter-spacing: 0.8px;
    color: var(--navy);
    text-transform: uppercase;
    white-space: nowrap;
  }
  .brand__slogan {
    margin-top: 4px;
    padding-top: 3px;
    border-top: 1px solid var(--red);
    font-weight: 700;
    font-size: 6.2px;
    letter-spacing: 0.4px;
    color: var(--navy);
    text-transform: uppercase;
    white-space: nowrap;
  }

  .letter {
    position: absolute;
    left: 27px; top: 182px;
    width: 415px;
    font-size: 7.9px;
    line-height: 8.6px;
    color: var(--ink);
  }
  .letter__salutation { font-size: 7.6px; margin-bottom: 17px; text-transform: uppercase; }
  .letter p.letter__para { text-align: justify; margin-bottom: 8.6px; }
  .letter__signoff { text-align: right; font-size: 7.6px; margin-top: 10px; text-transform: uppercase; }

  .contact-bar {
    position: absolute;
    left: 0; top: 616px;
    width: 470px;
    height: 2px;
    background: var(--red);
  }
  .contact-icon {
    position: absolute;
    top: 609px;
    width: 16px; height: 16px;
  }
  .contact-block {
    position: absolute;
    top: 633px;
    font-size: 7.4px;
    line-height: 8.4px;
    text-align: center;
    color: #111;
    white-space: nowrap;
    transform: translateX(-50%);
  }
</style>
</head>
<body>

<section class="letterhead letterhead--filled">
  <svg class="backdrop-mark" viewBox="0 0 400 430" role="img" aria-label="Faint brand backdrop shape">
    <circle cx="200" cy="230" r="190" fill="var(--ghost-grey)" opacity="0.55"/>
  </svg>
  <svg class="corner corner--top" viewBox="0 0 160 143"><polygon points="0,0 160,0 0,143" fill="var(--navy)"/></svg>

  <header class="brand">
    <div class="brand__badge"></div>
    <div class="brand__name">Ridgeline Build Network</div>
    <div class="brand__slogan">Plan. Partner. Build Together.</div>
  </header>

  <article class="letter">
    <p class="letter__salutation">Lorem ipsum</p>
    <p class="letter__para">Lorem ipsum dolor sit amet, consectetur adipiscing elit. Sed a augue eros. Sed sed porttitor diam, sed placerat neque. Phasellus pretium felis orci, vitae tincidunt mauris vulputate in. Cras sodales eget diam at viverra. Nulla quis mi lobortis libero luctus posuere. In non tortor vitae odio feugiat tristique. Sed semper tortor et consectetur suscipit. Donec nisl sapien, ullamcorper eget sagittis vel, iaculis in mi. Donec efficitur nulla in turpis placerat, at molestie neque tincidunt. Vestibulum luctus tincidunt elit, a aliquet erat convallis vel.</p>
    <p class="letter__para">Fusce lacinia condimentum quam nec venenatis. Phasellus tristique, dolor non cursus rutrum, mi dolor convallis ipsum, vel gravida nulla mauris elementum diam. Praesent ut facilisis arcu. Morbi imperdiet eu urna venenatis eleifend. Donec quis risus orci. Nullam elementum velit nisi, a consequat risus varius vitae. Vestibulum at ipsum dolor. Phasellus mattis pellentesque consequat. Phasellus feugiat magna lorem, sed bibendum libero facilisis et. Proin cursus elit eu neque fringilla, sed fermentum diam consectetur. Donec molestie sed orci sit amet iaculis. Fusce molestie vel massa vel tempus. Aliquam erat volutpat. Suspendisse ut orci quam. Duis tristique hendrerit nisi eu laoreet. Vivamus vulputate, ante in aliquet mollis, metus erat tincidunt sem, at feugiat velit massa id lectus.</p>
    <p class="letter__para">Proin ullamcorper, orci eget pulvinar lacinia, nulla mi scelerisque nisl, eu porta lorem lorem sit amet nisi. Lorem ipsum dolor sit amet, consectetur adipiscing elit. Praesent felis nisi, hendrerit ultricies enim eu, ultrices pellentesque felis. Nunc rutrum vitae arcu vel vehicula. Phasellus fringilla velit quis lectus eleifend, eu mollis metus pulvinar. Nam eget ex luctus, fringilla magna sit amet, condimentum purus. Cras vitae erat rhoncus, porta nisi vel, interdum magna. Vivamus at nibh ullamcorper leo tempor malesuada sed in nibh. Cras finibus felis id aliquet tincidunt.</p>
    <p class="letter__para">Nunc vulputate vehicula dictum. Aliquam pretium eros sed leo aliquam, in euismod neque aliquam. Aliquam fringilla sem in dolor tempor luctus. Proin posuere, lacus vitae mollis efficitur, erat quam mollis nisi, vel mattis neque dui ut ipsum. Mauris in lacus diam. Integer odio lacus, lobortis a massa id, tempus molestie felis. Maecenas ornare pretium felis. Nulla facilisi. Nulla mattis a turpis mattis semper. Duis semper odio accumsan viverra pellentesque. Integer egestas tempor dolor, a aliquet lacus eleifend ut. Vestibulum eu vulputate justo. Donec egestas mollis ante id eleifend. Vivamus consectetur dapibus augue, quis iaculis magna pulvinar sit amet.</p>
    <p class="letter__para">Aliquam erat volutpat. Morbi ac imperdiet mi, quis feugiat ante. Proin sodales porttitor odio quis faucibus. Morbi vitae luctus mauris. Praesent eu suscipit arcu. Quisque euismod, dolor ac aliquam dapibus, tellus tellus maximus metus, at sollicitudin nisl risus in nibh. Aliquam ut lectus est. Integer varius vulputate gravida. Aenean sit amet magna non arcu lobortis congue. Nullam ac quam magna.</p>
    <p class="letter__signoff">Lorem ipsum</p>
  </article>

  <div class="contact-bar"></div>
  <svg class="corner corner--bottom" viewBox="0 0 113 98"><polygon points="113,0 113,98 0,98" fill="var(--red)"/></svg>
  <svg class="contact-icon" style="left:61px" viewBox="0 0 16 16" aria-hidden="true"><circle cx="8" cy="8" r="7" fill="var(--red)"/><circle cx="8" cy="8" r="3.6" fill="none" stroke="#fff" stroke-width="1"/><line x1="4.4" y1="8" x2="11.6" y2="8" stroke="#fff" stroke-width="0.8"/><ellipse cx="8" cy="8" rx="1.6" ry="3.6" fill="none" stroke="#fff" stroke-width="0.8"/></svg>
  <svg class="contact-icon" style="left:173px" viewBox="0 0 16 16" aria-hidden="true"><circle cx="8" cy="8" r="7" fill="var(--red)"/><path d="M4.5 9.5 h7 v1.8 h-7z M5.5 9.5 l1-3 h3 l1 3" fill="#fff"/><rect x="4.8" y="5" width="6.4" height="1.2" rx="0.5" fill="#fff"/></svg>
  <svg class="contact-icon" style="left:291px" viewBox="0 0 16 16" aria-hidden="true"><circle cx="8" cy="8" r="7" fill="var(--red)"/><path d="M8 4 L12 7.6 H11 V11.5 H5 V7.6 H4 Z" fill="#fff"/><rect x="7.1" y="9" width="1.8" height="2.5" fill="var(--red)"/></svg>

  <div class="contact-block" style="left:69px">info@ridgelinebuildnet.example<br>www.ridgelinebuildnet.example</div>
  <div class="contact-block" style="left:181px">916-555-0148<br>916-555-0172</div>
  <div class="contact-block" style="left:300px">487 Willowmere Ave, Ste 210<br>Folsom, CA 95699</div>
</section>

<section class="letterhead letterhead--blank">
  <svg class="backdrop-mark" viewBox="0 0 400 430" role="img" aria-label="Faint brand backdrop shape">
    <circle cx="200" cy="230" r="190" fill="var(--ghost-grey)" opacity="0.9"/>
  </svg>
  <svg class="corner corner--top" viewBox="0 0 160 143"><polygon points="0,0 160,0 0,143" fill="var(--navy)"/></svg>

  <header class="brand">
    <div class="brand__badge"></div>
    <div class="brand__name">Ridgeline Build Network</div>
    <div class="brand__slogan">Plan. Partner. Build Together.</div>
  </header>

  <div class="contact-bar"></div>
  <svg class="corner corner--bottom" viewBox="0 0 113 98"><polygon points="113,0 113,98 0,98" fill="var(--red)"/></svg>
  <svg class="contact-icon" style="left:61px" viewBox="0 0 16 16" aria-hidden="true"><circle cx="8" cy="8" r="7" fill="var(--red)"/><circle cx="8" cy="8" r="3.6" fill="none" stroke="#fff" stroke-width="1"/><line x1="4.4" y1="8" x2="11.6" y2="8" stroke="#fff" stroke-width="0.8"/><ellipse cx="8" cy="8" rx="1.6" ry="3.6" fill="none" stroke="#fff" stroke-width="0.8"/></svg>
  <svg class="contact-icon" style="left:173px" viewBox="0 0 16 16" aria-hidden="true"><circle cx="8" cy="8" r="7" fill="var(--red)"/><path d="M4.5 9.5 h7 v1.8 h-7z M5.5 9.5 l1-3 h3 l1 3" fill="#fff"/><rect x="4.8" y="5" width="6.4" height="1.2" rx="0.5" fill="#fff"/></svg>
  <svg class="contact-icon" style="left:291px" viewBox="0 0 16 16" aria-hidden="true"><circle cx="8" cy="8" r="7" fill="var(--red)"/><path d="M8 4 L12 7.6 H11 V11.5 H5 V7.6 H4 Z" fill="#fff"/><rect x="7.1" y="9" width="1.8" height="2.5" fill="var(--red)"/></svg>

  <div class="contact-block" style="left:69px">info@ridgelinebuildnet.example<br>www.ridgelinebuildnet.example</div>
  <div class="contact-block" style="left:181px">916-555-0148<br>916-555-0172</div>
  <div class="contact-block" style="left:300px">487 Willowmere Ave, Ste 210<br>Folsom, CA 95699</div>
</section>

</body>
</html>
```